Design a few pages of a luxury magazine for the Prestige Aubergerie Lyon

We need a luxury design for our magazine. See the inDesign pages of the current version attached (zip).

Please work primarily on the first double page (Inventez le luxe de demain) that contains only one photo with legend, a title and the text both in French and English. It must be made clear that the text is the same in two different languages (it is not clear enough here).

You can also work on the other two double pages selected. Feedback will be provided and the 10 best pages will be submitted to a vote at the end of the project timespan.

The most important is a classy and luxury design, this will be printed on expensive paper.

See the full brochure here: https://www.prestigeaubergerie.com/brochure/#page=4

Target Market(s)

Students and parents

Industry/Entity Type

Education

Colors

Designer to choose colors to be used in the design.

Requirements
Must have
• Luxury magazine layout, see:
• https://www.findwerk.com/search?q=luxury+magazine+layout&client=safari&rls=en&source=lnms&tbm=isch&sa=X&ved=0ahUKEwitoIDmit7fAhUVShUIHXC2Cd4Q_AUIDigB&biw=1010&bih=702
Nice to have
• The color of the cover that should be used for blue and grey is #393d49.
• Our font for serif titles (from the logo) is Adobe TRAJAN.
Should not have
• flashy colors

```html
<!DOCTYPE html>
<html lang="fr">
<head>
<meta charset="utf-8">
<title>Prestige Aubergerie – Inventez le luxe de demain</title>
<link rel="stylesheet" href="https://fonts.googleapis.com/css2?family=Cinzel:wght@400&family=Fira+Sans:wght@300;400&display=swap">
<style>
  :root {
    --ink: #393d49;
    --band: #2c3240;
    --frame: #2c3240;
    --paper: #ffffff;
    --text: #2a2e38;
    --muted: #8a8d94;
  }
  html, body { margin: 0; padding: 0; overflow: hidden; }
  body { width: 1200px; height: 763px; background: var(--paper); }
  .spread {
    position: relative;
    width: 1200px; height: 763px;
    overflow: hidden;
    background: var(--paper);
    font-family: "Fira Sans", Arial, sans-serif;
    color: var(--text);
  }
  .kicker, .subkicker {
    position: absolute; left: 58px; margin: 0;
    font-size: 13.5px; font-weight: 300; color: var(--ink);
  }
  .headline {
    position: absolute; left: 57px; margin: 0;
    font-family: "Cinzel", "Times New Roman", serif;
    font-weight: 400; font-size: 32px; line-height: 31px;
    letter-spacing: 1.2px; color: var(--ink);
  }
  .rule {
    position: absolute; left: 58px;
    width: 36px; height: 3px; background: var(--ink);
  }
  .body-copy {
    position: absolute; left: 58px; width: 338px;
    font-size: 8.6px; line-height: 11.2px; font-weight: 400;
  }
  .body-copy p { margin: 0 0 11px; }
  .folio {
    position: absolute; top: 714px;
    font-size: 13px; font-weight: 300; color: var(--ink);
  }
  .folio::after {
    content: ""; display: block; width: 8px; height: 1px;
    background: var(--muted); margin-top: 6px;
  }
  .spine-band {
    position: absolute; left: 558px; top: 0;
    width: 45px; height: 763px; background: var(--band);
  }
  .frame {
    position: absolute; left: 709px; top: 50px;
    width: 447px; height: 517px;
    border: 6px solid var(--frame);
  }
  .team-photo {
    position: absolute; left: 470px; top: 85px;
    width: 656px; height: 542px;
    background:
      radial-gradient(ellipse at 55% 75%, rgba(214,190,150,.85) 0%, rgba(214,190,150,0) 45%),
      radial-gradient(ellipse at 50% 30%, rgba(240,205,140,.55) 0%, rgba(240,205,140,0) 40%),
      linear-gradient(180deg, #4a4538 0%, #2f2c25 45%, #6f6450 70%, #c9b796 100%);
  }
  .fold-line {
    position: absolute; left: 603px; top: 85px;
    width: 1px; height: 542px; background: rgba(20,22,28,.7);
  }
  .caption {
    position: absolute; left: 804px; top: 640px; width: 322px;
    font-size: 8.6px; line-height: 11.2px;
  }
  .caption p { margin: 0 0 7px; }
</style>
</head>
<body>
<main class="spread">
  <p class="kicker" style="top:74px">à la Prestige Aubergerie</p>
  <h1 class="headline" style="top:92px">Inventez le luxe<br>de demain</h1>
  <div class="rule" style="top:168px"></div>
  <div class="body-copy" lang="fr" style="top:188px">
    <p>Depuis sa création il y a 30 ans, notre école garde le même objectif : que chaque étudiant acquière les compétences et développe les talents essentiels pour briller dans l'univers du luxe. Première école dédiée à l'hôtellerie de luxe, la Prestige Aubergerie délivre un Bachelor et un Master of Science in International Tourism and Hospitality Management, deux grades universitaires anglais.</p>
    <p>Cette combinaison du luxe à la française et du management anglosaxon donne toutes les clés à nos étudiants pour s'assurer une place privilégiée dans l'univers du luxe en France et à l'international.</p>
    <p>Grâce à l'excellence académique de nos programmes, la dimension internationale de nos formations et l'immersion professionnelle à travers des stages dans les plus prestigieux hôtels du monde, tous nos diplômés sont assurés de faire carrière dans le secteur de leur choix à un poste stratégique. La moitié d'entre eux signent un CDI avant même la fin de leur dernier stage.</p>
  </div>

  <h2 class="headline" lang="en" style="top:395px">Invent tomorrow's<br>luxuries</h2>
  <p class="subkicker" style="top:456px">at the Prestige Aubergerie</p>
  <div class="rule" style="top:488px"></div>
  <div class="body-copy" lang="en" style="top:506px">
    <p>Since its foundation 30 years ago, our school has had only on objective: that each student acquires the skills and develops the essential talents they require to shine within the luxury sector. The Prestige Aubergerie is the first Higher Education establishment dedicated to luxury hotel training: we offer a Bachelor's and a Master's degree in International Tourism and Hospitality Management.</p>
    <p>This combination of French-style luxury and Anglo-Saxon management gives our students the key elements they need to ensure a privileged position within the luxury industry both in France and internationally.</p>
    <p>The academic excellence of our programmes, the international dimension of our training and our professional work placements at the most prestigious hotels in the world all ensure that our graduates are certain to secure a career in a strategic role in the luxury sector. Half of our students sign a permanent contract before they even finish their final work placement.</p>
  </div>

  <span class="folio" style="left:39px">2</span>

  <div class="spine-band"></div>
  <div class="frame"></div>
  <div class="team-photo" role="img" aria-label="Photo of the four-person management team posing in an elegant hotel salon with a green velvet sofa, chandeliers and tall windows"></div>
  <div class="fold-line"></div>

  <div class="caption">
    <p lang="fr">De gauche à droite, l'équipe de Direction de la Prestige Aubergerie dans les salons du Palais Vendôme : Léon Marchetti, Vice-Président, Inès Valbonne, Directeur des opérations, Claire Dumesnil, Responsable pédagogique, et Mathieu Roussel, Président</p>
    <p lang="en">From left to right, the PA Management team at the Palais Vendôme: Léon Marchetti, Vice-President, Inès Valbonne, Operations Manager, Claire Dumesnil, Education Manager and Mathieu Roussel, President</p>
  </div>

  <span class="folio" style="left:1162px">3</span>
</main>
</body>
</html>
```